Caldrow Supplies Business Card

Professional business card that stand out to our potential customers. Front and back with clean modern design

Industry/Entity Type

Oil and gas

Contact Information for Business Card

Name, address, website , office phone and cell number

Requirements
Must have
• Editable files for each employee

```html
<!DOCTYPE html>
<html lang="en">
<head>
<meta charset="UTF-8">
<title>Caldrow Supplies Business Card</title>
<link href="https://fonts.googleapis.com/css2?family=Roboto:wght@400;500;700&display=swap" rel="stylesheet">
<style>
  :root {
    --bg: #2a2a2a;
    --card: #f7f7f5;
    --red: #e3202a;
    --blue: #1fa9d1;
    --ink: #333333;
    --white: #ffffff;
  }
  * { margin: 0; padding: 0; box-sizing: border-box; }
  html, body {
    width: 1200px; height: 852px; overflow: hidden;
    background: var(--bg);
    font-family: "Roboto", Arial, sans-serif;
  }
  .stage {
    position: relative; width: 1200px; height: 852px;
  }
  .card {
    position: absolute;
    width: 560px; height: 320px;
    background: var(--card);
    border-radius: 22px;
    overflow: hidden;
    box-shadow: 0 10px 24px rgba(0,0,0,0.45);
  }
  .card-front { left: 150px; top: 70px; }
  .card-back { left: 490px; top: 460px; }

  /* front */
  .front-brand {
    position: absolute; left: 0; right: 0; top: 128px;
    display: flex; align-items: center; justify-content: center; gap: 14px;
  }
  .brand-square {
    width: 30px; height: 30px; background: var(--red);
  }
  .brand-name {
    font-size: 34px; font-weight: 700; color: var(--red);
    letter-spacing: 0.5px; text-transform: uppercase;
  }
  .edge {
    position: absolute; left: 0; bottom: 0; width: 100%; height: 10px;
  }

  /* back */
  .back-brand {
    position: absolute; left: 34px; top: 110px; width: 250px;
    font-size: 38px; font-weight: 700; color: var(--red);
    line-height: 1.1; text-transform: uppercase;
  }
  .contact {
    position: absolute; left: 318px; top: 46px; color: var(--ink);
  }
  .contact-name {
    font-size: 21px; font-weight: 500; color: var(--blue);
  }
  .contact-title {
    font-size: 13px; margin-top: 3px;
  }
  .contact-address {
    font-size: 13px; line-height: 1.35; margin-top: 22px;
  }
  .contact-list {
    list-style: none; margin-top: 4px; font-size: 13px; line-height: 1.45;
  }
  .contact-list li { display: flex; align-items: center; gap: 8px; }
  .contact-list svg { width: 11px; height: 11px; fill: var(--red); }
  .company-tab {
    position: absolute; right: 0; bottom: 10px;
    width: 250px; height: 58px;
    background: var(--blue);
    border-top-left-radius: 20px;
    color: var(--white); font-size: 15px; font-weight: 500;
    display: flex; align-items: center; justify-content: center;
  }
</style>
</head>
<body>
<main class="stage">

  <section class="card card-front" aria-label="Card front">
    <div class="front-brand">
      <span class="brand-square"></span>
      <span class="brand-name">Caldrow Supplies</span>
    </div>
    <svg class="edge" viewBox="0 0 560 10" preserveAspectRatio="none" aria-hidden="true">
      <polygon points="0,6 396,6 410,0 560,0 560,10 0,10" fill="var(--red)"/>
      <polygon points="410,0 560,0 560,10 396,10" fill="var(--blue)"/>
    </svg>
  </section>

  <section class="card card-back" aria-label="Card back">
    <div class="back-brand">Caldrow Supplies</div>

    <div class="contact">
      <p class="contact-name">Marcus Hale</p>
      <p class="contact-title">Managing Director</p>
      <p class="contact-address">214 Ridgeline Ave Suite 5<br>Midland, TX 79701</p>
      <ul class="contact-list">
        <li><svg viewBox="0 0 12 12"><path d="M3 1l2 2-1 1.5c.8 1.6 1.9 2.7 3.5 3.5L9 7l2 2-1.5 2C5 10.5 1.5 7 1 2.5z"/></svg>(432)555-0187</li>
        <li><svg viewBox="0 0 12 12"><path d="M1 3h10v6H1z M1 3l5 4 5-4" stroke="var(--card)" stroke-width="1"/></svg>sales@caldrowsupplies.com</li>
        <li><svg viewBox="0 0 12 12"><circle cx="6" cy="6" r="5"/></svg>www.caldrowsupplies.com</li>
      </ul>
    </div>

    <div class="company-tab">Caldrow Supplies LLC</div>
    <svg class="edge" viewBox="0 0 560 10" preserveAspectRatio="none" aria-hidden="true">
      <rect x="0" y="0" width="310" height="10" fill="var(--red)"/>
      <rect x="310" y="0" width="250" height="10" fill="var(--blue)"/>
    </svg>
  </section>

</main>
</body>
</html>
```